R.T. Framers Postcard Design

We need a postcard designed around the utility rebates for window installations. For customers who have Electric heated homes can receive $6 per square foot for each window and patio door and for Natural gas heated homes, they can get $75.00 per window and patio door. The $6 per square foot for electric heated customers is the better rebate averaging about $1000.00 for a house with 10 windows and a patio door. Our Company colors are maroon, black and white, we would like to have a post card designed around these colors. The postcard should be designed to share about these 2 rebates and having a window installation theme. You can use pictures off of our website...www.rtframers-example.com

Target Market(s)

Homeowners with electric heat or Natural gas heat

Industry/Entity Type

Utility

Requirements
Must have
• Blank white square on the back for me to hand write address information.

```html
<!DOCTYPE html>
<html lang="en">
<head>
<meta charset="utf-8">
<title>R.T. Framers Rebate Postcard</title>
<link href="https://fonts.googleapis.com/css2?family=Montserrat:wght@600;700;800&family=Questrial&family=Source+Sans+3:wght@700&display=swap" rel="stylesheet">
<style>
  :root {
    --maroon: #a0161c;
    --maroon-deep: #5e0a0e;
    --red-bright: #c42026;
    --black: #1a1a1a;
    --ink: #2b2b2b;
    --white: #ffffff;
    --rule: #d9d9d9;
    --stamp-border: #d0d0d0;
  }
  * { box-sizing: border-box; margin: 0; padding: 0; }
  html, body { width: 1200px; height: 930px; overflow: hidden; background: var(--white); }
  .postcard { position: relative; width: 1200px; height: 930px; background: var(--white); }

  .front {
    position: absolute; left: 0; top: 0; width: 580px; height: 765px;
    background: linear-gradient(180deg, var(--red-bright) 0%, var(--maroon) 40%, var(--maroon-deep) 80%);
    overflow: hidden;
  }
  .front-floor {
    position: absolute; left: 0; top: 612px; width: 580px; height: 153px;
    background: linear-gradient(180deg, #5a5a5a 0%, #2a2a2a 40%, #111 100%);
  }
  .brand-banner {
    position: absolute; left: -20px; top: 48px; width: 578px; height: 170px;
    background: linear-gradient(180deg, #ffffff 0%, #f2f2f2 70%, #d8d8d8 100%);
    border-radius: 0 60px 60px 0;
    box-shadow: 0 14px 24px rgba(0,0,0,0.35);
    transform: rotate(1.5deg);
    display: flex; align-items: center; padding-left: 62px; gap: 20px;
  }
  .brand-mark { width: 96px; height: 96px; background: var(--maroon); border-radius: 8px; flex: none; }
  .brand-text { display: flex; flex-direction: column; }
  .brand-name {
    font-family: "Montserrat", sans-serif; font-weight: 800; font-size: 58px;
    color: var(--maroon); line-height: 1; letter-spacing: -1px;
  }
  .brand-tagline {
    font-family: "Source Sans 3", sans-serif; font-weight: 700; font-size: 21px;
    color: var(--black); margin-top: 8px;
  }
  .rebate-copy {
    position: absolute; left: 39px; top: 272px; width: 520px;
    font-family: "Montserrat", sans-serif; font-weight: 700; font-size: 25px;
    line-height: 33px; color: var(--white);
  }
  .room-photo {
    position: absolute; top: 518px; height: 120px; border-radius: 4px;
    box-shadow: 0 3px 8px rgba(0,0,0,0.5);
  }
  .room-photo.bright { left: 30px; width: 180px; background: linear-gradient(135deg, #f4f1ea, #c9c2b3 60%, #7a3a2a); }
  .room-photo.warm { left: 220px; width: 155px; background: linear-gradient(135deg, #b5703f, #e8dcc0 55%, #8a5a35); }
  .room-photo.garden { left: 384px; width: 180px; background: linear-gradient(135deg, #d8c98a, #9fb86a 50%, #2f3a28); }
  .site-link {
    position: absolute; right: 16px; top: 708px;
    display: flex; align-items: center; gap: 10px;
    font-family: "Montserrat", sans-serif; font-weight: 700; font-size: 34px; color: var(--white);
  }
  .site-dot { width: 38px; height: 38px; border-radius: 50%; background: var(--red-bright); border: 3px solid var(--white); }

  .mailing-address {
    position: absolute; left: 597px; top: 62px; width: 300px; text-align: center;
    font-family: "Questrial", sans-serif; font-size: 27px; line-height: 33px; color: var(--ink);
  }
  .stamp-box {
    position: absolute; left: 900px; top: 27px; width: 272px; height: 274px;
    border: 2px solid var(--stamp-border); background: var(--white);
  }
  .write-line { position: absolute; left: 640px; width: 514px; height: 3px; background: var(--rule); }
</style>
</head>
<body>
<div class="postcard">
  <section class="front">
    <div class="front-floor"></div>
    <div class="brand-banner">
      <div class="brand-mark"></div>
      <div class="brand-text">
        <span class="brand-name">R.T. Framers</span>
        <span class="brand-tagline">Custom windows &amp; door installations</span>
      </div>
    </div>
    <p class="rebate-copy">For customers who have Electric heated homes can receive $6 per square foot for each window and patio door and for Natural gas heated homes, they can get $75.00 per window and patio door.</p>
    <div class="room-photo bright" role="img" aria-label="Bright room with large white-framed windows"></div>
    <div class="room-photo warm" role="img" aria-label="Living room with new window and sofa"></div>
    <div class="room-photo garden" role="img" aria-label="Lounge with picture window facing a garden"></div>
    <div class="site-link"><span class="site-dot"></span>rtframers-example.com</div>
  </section>

  <address class="mailing-address">2715 Alder Grove Road NE<br>Pinecrest<br>Washington<br>98999<br>United States</address>
  <div class="stamp-box"></div>
  <div class="write-line" style="top:410px"></div>
  <div class="write-line" style="top:501px"></div>
  <div class="write-line" style="top:591px"></div>
  <div class="write-line" style="top:681px"></div>
</div>
</body>
</html>
```